Business Card Design Project

I need the following:

Logo -
Name - Dale Prewitt
Title - Customer Experience Officer
Web - www.bvrh.net
Phone - 555-417-3068
Updates

Project Deadline Extended
Reason: I launched the project later than anticipated. I look forward to seeing your designs. Dale

Industry/Entity Type

Business

```html
<!DOCTYPE html>
<html lang="en">
<head>
<meta charset="utf-8">
<title>Bridgeview Relay Holdings – Business Card</title>
<link href="https://fonts.googleapis.com/css2?family=Exo+2:wght@400;500;800&display=swap" rel="stylesheet">
<style>
  :root {
    --backdrop: #a8a8a8;
    --card-white: #ffffff;
    --ink: #111111;
    --brand-blue: #1a82c4;
    --brand-blue-light: #2bb6ec;
    --brand-blue-deep: #0b4f8a;
    --silver: #c9ccd0;
    --panel-dark: #1a1c1f;
    --panel-darker: #0b0c0e;
    --text-light: #f2f2f2;
  }
  * { margin: 0; padding: 0; box-sizing: border-box; }
  html, body {
    width: 1200px; height: 900px; overflow: hidden;
    background: var(--backdrop);
    font-family: "Exo 2", sans-serif;
  }
  .card {
    position: absolute; left: 160px; top: 180px;
    width: 880px; height: 540px;
    border-radius: 28px; overflow: hidden;
    background: var(--card-white);
    box-shadow: 0 18px 40px rgba(0,0,0,0.28);
  }
  .brand {
    position: absolute; left: 56px; top: 36px;
    display: flex; align-items: center; gap: 34px;
  }
  .brand-mark {
    width: 160px; height: 160px; border-radius: 50%;
    background: radial-gradient(circle at 38% 32%, var(--brand-blue-light), var(--brand-blue) 45%, var(--brand-blue-deep) 100%);
  }
  .brand-name {
    font-weight: 800; font-size: 36px; line-height: 0.98;
    letter-spacing: 1px; color: var(--ink); text-transform: uppercase;
  }
  .brand-url {
    display: flex; align-items: center; gap: 10px; margin-top: 8px;
    font-weight: 800; font-size: 15px; color: var(--brand-blue);
  }
  .brand-url::before, .brand-url::after {
    content: ""; flex: 1; height: 2px; background: var(--brand-blue);
  }
  .accent-band {
    position: absolute; left: 0; top: 230px; width: 100%; height: 26px;
    background: linear-gradient(90deg, var(--brand-blue) 0%, var(--brand-blue-light) 100%);
  }
  .silver-rule {
    position: absolute; left: 0; top: 256px; width: 100%; height: 5px;
    background: linear-gradient(180deg, #f4f4f4, var(--silver));
  }
  .contact-panel {
    position: absolute; left: 0; top: 261px; width: 100%; height: 279px;
    background: linear-gradient(180deg, var(--panel-dark), var(--panel-darker));
    padding: 32px 0 0 56px;
  }
  .person-name {
    font-weight: 500; font-size: 38px; color: var(--brand-blue); line-height: 1;
  }
  .person-title {
    font-weight: 400; font-size: 20px; color: var(--text-light); margin-top: 6px;
  }
  .contact-list { list-style: none; margin-top: 40px; }
  .contact-item {
    display: flex; align-items: center; gap: 14px;
    font-weight: 500; font-size: 34px; color: var(--text-light);
    letter-spacing: 1px; line-height: 1; margin-bottom: 18px;
  }
  .contact-icon { width: 36px; height: 36px; flex: none; }
</style>
</head>
<body>
  <div class="card">
    <div class="brand">
      <div class="brand-mark"></div>
      <div class="brand-text">
        <div class="brand-name">Bridgeview<br>Relay<br>Holdings</div>
        <div class="brand-url">www.bvrh.net</div>
      </div>
    </div>

    <div class="accent-band"></div>
    <div class="silver-rule"></div>

    <div class="contact-panel">
      <div class="person-name">Dale Prewitt</div>
      <div class="person-title">Customer Experience Officer</div>
      <ul class="contact-list">
        <li class="contact-item">
          <svg class="contact-icon" viewBox="0 0 36 36" aria-hidden="true">
            <circle cx="18" cy="18" r="16" fill="none" stroke="#1a82c4" stroke-width="2.5"/>
            <path d="M12.5 10.5c1-.8 2-.6 2.6.3l1.6 2.6c.5.8.3 1.6-.4 2.2l-1 .8c.7 2 2.3 3.8 4.3 4.8l.9-1c.6-.7 1.5-.8 2.200-.3l2.5 1.7c.9.6 1 1.6.2 2.5-1.3 1.5-3 2.3-5 1.3-4.6-2.2-8-6.1-9.1-10.3-.5-2 .4-3.6 1.2-4.6z" fill="#1a82c4"/>
          </svg>
          555-417-3068
        </li>
        <li class="contact-item">
          <svg class="contact-icon" viewBox="0 0 36 36" aria-hidden="true">
            <circle cx="18" cy="18" r="16" fill="none" stroke="#1a82c4" stroke-width="2.5"/>
            <g fill="none" stroke="#1a82c4" stroke-width="1.6">
              <circle cx="18" cy="18" r="9"/>
              <ellipse cx="18" cy="18" rx="4" ry="9"/>
              <line x1="9" y1="18" x2="27" y2="18"/>
              <line x1="10.5" y1="13.5" x2="25.5" y2="13.5"/>
              <line x1="10.5" y1="22.5" x2="25.5" y2="22.5"/>
            </g>
          </svg>
          www.bvrh.net
        </li>
      </ul>
    </div>
  </div>
</body>
</html>
```